Wordpress design for my private practice website - Psychotherapist

I would like a simple, clean, and elegant design for my private practice website. I work with both adults and children so I'd like it to appeal to both. However, since parents make the choice as to where to send their child for therapy, I want it to appeal to adults more. I would like the pictures on the site to have a calming effect - maybe using sand and water and rocks. I am attaching files with my company logo. I would also like my name incorporated into the header - Colette Brannigan, LCSW, Registered Play Therapist. I've also uploaded a picture of myself for my About Page.

I like the design of these 2 website and want something similar:
www.drlorapenwick.example
www.harwood-tallis.example

I would like a home page that highlights a calming graphic across the entire top of the page as well as my practice logo and my name.

I'd like a link to social media sites on the top of the homepage - facebook, pinterest.

I want a simple bar across the top with the following tabs:
Home
About Me (subtabs Who I Am, Specialties and Approach)
Counseling Services (subtabs Individual Counseling, Play Therapy, Sandplay Therapy,)
Fees
FAQs
Contact Me (would love this to be a fill in the blank contact form that sends info to my email address - should include name, phone number, email and a comment box for more information requested)
Blog (this will link with another wordpress blog)

Target Market(s)

Parents of children under age 12 with behavioral problems or are dealing with the breakup of their family through divorce - looking for someone to work with their young child. I also work with Adults that are overwhelmed and worried - often women that have many life stressors and are feeling burnt out on life and meeting everyone's needs. Families going through some type of trauma, including divorce or grief work. I also work with individuals going through a transition of religious beliefs - often exiting the religion of their youth and undergoing a crisis of faith at midlife.

Industry/Entity Type

Mental Health

Contact Information for Business Card

Colette Brannigan, LCSW
Registered Play Therapist
4917 Wexmoor Lane
Idaho Falls, Idaho 83404
(208)555-0187
www.stillbrookcounseling.example

On the opposite side, I'd like an appointment reminder area - with the following text:

Your next appointment is
_____/______/______ at ______am/pm
Please give 24 hrs notice if you need to cancel your appointment.

Coding

Coded - Design and coding required

Number of Pages Required

5+ page

Font styles to use
Sans Serif

Colors
33a6d7
9bcb3c
0355a3

Requirements
Must have
• I'd like it to be a wordpress site. I'm such a newby at web design - but I need to be able to add content and manage the site myself once it is up and running.
Nice to have
• I like the design of these 2 websites and want something similar:
• www.drlorapenwick.example
• www.harwood-tallis.example
• They are clean, easy to navigate and calming.
Should not have
• Should not look like a childcare website.

```html
<!DOCTYPE html>
<html lang="en">
<head>
<meta charset="utf-8">
<title>Colette Brannigan – About</title>
<link href="https://fonts.googleapis.com/css2?family=Open+Sans:wght@300;400&family=Cormorant+Garamond:wght@700&family=Lobster+Two:ital,wght@1,700&display=swap" rel="stylesheet">
<style>
  :root {
    --ink: #5f5f5f;
    --ink-soft: #777777;
    --brand-blue: #27608f;
    --header-bg: #ffffff;
    --content-bg: #fcfbfc;
    --rule: #e6e4e6;
    --dropdown-bg: #b8b8b8;
    --dropdown-line: #cfcfcf;
    --icon: #555555;
    --footer-icon: #d9d9d9;
    --white: #ffffff;
    --hero-top: #6c717a;
    --hero-bottom: #7a6d63;
    --portrait-top: #cbb988;
    --portrait-bottom: #a39c78;
  }
  * { margin: 0; padding: 0; box-sizing: border-box; }
  html, body { width: 1200px; height: 1145px; overflow: hidden; }
  body {
    position: relative;
    background: var(--header-bg);
    font-family: "Open Sans", Arial, sans-serif;
    font-weight: 300;
    color: var(--ink);
  }
  .site-header { position: absolute; top: 0; left: 0; width: 1200px; height: 158px; }
  .brand { position: absolute; top: 20px; left: 0; width: 1200px; text-align: center; }
  .brand-dot {
    display: block; width: 44px; height: 44px; margin: 0 auto 10px;
    border-radius: 50%; background: var(--brand-blue);
  }
  .brand-name {
    font-weight: 300; color: var(--ink-soft); letter-spacing: 5px;
    font-size: 16px; line-height: 20px; text-transform: uppercase;
  }
  .brand-sub { font-size: 8px; letter-spacing: 3.5px; line-height: 12px; font-weight: 300; color: var(--ink-soft); }
  .social-top { position: absolute; top: 119px; left: 987px; display: flex; gap: 23px; list-style: none; }
  .social-top li { width: 12px; height: 12px; border-radius: 50%; background: var(--icon); }

  .hero {
    position: absolute; top: 158px; left: 0; width: 1200px; height: 335px;
    background: linear-gradient(180deg, var(--hero-top) 0%, var(--hero-bottom) 100%);
  }
  .hero-title {
    position: absolute; left: 83px; top: 135px;
    font-family: "Cormorant Garamond", Georgia, serif; font-weight: 700;
    font-size: 29px; color: var(--white); letter-spacing: .2px;
  }
  .hero-role {
    position: absolute; left: 83px; top: 176px;
    font-family: "Lobster Two", cursive; font-style: italic; font-weight: 700;
    font-size: 16px; color: var(--white);
  }

  .main-nav { position: absolute; top: 493px; left: 0; width: 1200px; height: 75px; border-bottom: 1px solid var(--rule); }
  .main-nav a {
    position: absolute; top: 31px; font-size: 14px; font-weight: 400;
    color: var(--ink); text-decoration: none; white-space: nowrap;
  }
  .caret { display: inline-block; margin-left: 4px; vertical-align: middle; }
  .dropdown { position: absolute; top: 569px; left: 338px; width: 133px; background: var(--dropdown-bg); list-style: none; z-index: 3; }
  .dropdown li { color: var(--white); font-size: 12.5px; font-weight: 300; text-transform: uppercase; }
  .dropdown li:first-child { padding: 10px 0 10px 32px; border-bottom: 1px solid var(--dropdown-line); }
  .dropdown li:last-child { padding: 8px 10px 9px 15px; line-height: 22px; }

  .content { position: absolute; top: 657px; left: 0; width: 1200px; height: 381px; background: var(--content-bg); border-bottom: 1px solid var(--rule); }
  .portrait {
    position: absolute; top: 641px; left: 83px; width: 339px; height: 334px;
    border: 1px solid #c9c4b4;
    background: linear-gradient(180deg, var(--portrait-top) 0%, var(--portrait-bottom) 100%);
    z-index: 1;
  }
  .about-title { position: absolute; top: 634px; left: 445px; font-size: 27px; font-weight: 300; color: var(--ink-soft); z-index: 2; }
  .about-copy { position: absolute; left: 445px; width: 662px; font-size: 12.3px; line-height: 21px; color: var(--ink); z-index: 2; }
  .about-copy.first { top: 689px; }
  .about-copy.second { top: 879px; }

  .site-footer { position: absolute; top: 1038px; left: 0; width: 1200px; height: 107px; background: var(--content-bg); text-align: center; }
  .copyright { position: absolute; top: 21px; width: 1200px; font-size: 12.5px; color: var(--ink-soft); }
  .social-foot { position: absolute; top: 56px; left: 543px; display: flex; gap: 9px; list-style: none; }
  .social-foot li { width: 22px; height: 22px; border-radius: 50%; background: var(--footer-icon); }
</style>
</head>
<body>
  <header class="site-header">
    <div class="brand">
      <span class="brand-dot"></span>
      <div class="brand-name">Stillbrook</div>
      <div class="brand-sub">COUNSELING</div>
    </div>
    <ul class="social-top" aria-label="Social links">
      <li aria-label="Social profile"></li>
      <li aria-label="Social profile"></li>
      <li aria-label="Social profile"></li>
      <li aria-label="Social profile"></li>
    </ul>
  </header>

  <section class="hero" role="img" aria-label="Calming beach photograph with sand, sea and stacked stones">
    <h1 class="hero-title">Colette Brannigan,</h1>
    <p class="hero-role">Relationship Counselor</p>
  </section>

  <nav class="main-nav">
    <a style="left:303px">Home<svg class="caret" width="8" height="5" viewBox="0 0 8 5"><path d="M0.5 0.5 4 4 7.5 0.5" fill="none" stroke="#999" stroke-width="1"/></svg></a>
    <a style="left:383px">About</a>
    <a style="left:463px">Counseling Services<svg class="caret" width="8" height="5" viewBox="0 0 8 5"><path d="M0.5 0.5 4 4 7.5 0.5" fill="none" stroke="#999" stroke-width="1"/></svg></a>
    <a style="left:632px">Fees</a>
    <a style="left:702px">FAQs</a>
    <a style="left:776px">Contact</a>
    <a style="left:867px">Blog</a>
  </nav>
  <ul class="dropdown">
    <li>Who I Am</li>
    <li>Specialities and Approach</li>
  </ul>

  <main class="content"></main>
  <div class="portrait" role="img" aria-label="Portrait photograph of the counselor"></div>
  <h2 class="about-title">ABOUT</h2>
  <p class="about-copy first">Lorem ipsum dolor sit amet, consectetur adipiscing elit. Quisque nec tempor nunc. Proin vestibulum lacinia metus, vitae efficitur est luctus sed. Etiam neque felis, ullamcorper eu urna quis, consectetur pulvinar tortor. Vestibulum ullamcorper semper nisi, pretium molestie tortor scelerisque eu. Phasellus quis leo id leo tempus rutrum in eu massa. Ut felis nulla, dapibus id malesuada et, sodales eget velit. Aenean facilisis arcu quis pellentesque rhoncus. Nunc tempus ex vitae arcu sodales, eu efficitur est luctus. Nullam dolor leo, ornare vel faucibus vel, porta vel est. Phasellus at mauris id nunc mattis commodo vitae eget elit. Quisque et gravida nisi. Pellentesque sagittis mauris et iaculis volutpat. Ut vehicula a libero ultricies mattis. Ut cursus ligula auctor, vestibulum dolor eget, lobortis nibh. Fusce molestie volutpat interdum.</p>
  <p class="about-copy second">Nunc tempus ex vitae arcu sodales, eu efficitur est luctus. Nullam dolor leo, ornare vel faucibus vel, porta vel est. Phasellus at mauris id nunc mattis commodo vitae eget elit. Quisque et gravida nisi. Pellentesque sagittis mauris et iaculis volutpat.</p>

  <footer class="site-footer">
    <p class="copyright">© 2012 Colette Brannigan. All rights reserved.</p>
    <ul class="social-foot" aria-label="Social links">
      <li aria-label="Social profile"></li>
      <li aria-label="Social profile"></li>
      <li aria-label="Social profile"></li>
      <li aria-label="Social profile"></li>
    </ul>
  </footer>
</body>
</html>
```